TB - WESITE NEEDED PAGE: Clean / Modern / Pro & Dynamic

Tavlin-Brokers is a new insurance brokerage firm dealing exclusively with companies (BToB) providing the following property: Liabilities Insurance Insurances Automobile Insurance Insurances Construction% 26amp; Engineering Casualty Workmen 's Compensation Health Insurance Marime% 26amp; Transit Credit Insurance Young, Fast, Proactive and Dynamic we call ourselves Tavlin-Brokers because we are a "start-up" willing to make a difference in the market, bringing modernity and speed to our industry, still too bureaucratic / procedural / opaque uninitiated. We need something respecting the colors of our orange logtype; blue; white; black; easy to scroll, with simple information on the company; - who we are - our team (with the pictures) - what we do - what we do - contact us, contact us (google map) Luanda (Angola) Small company, just need something flashy / professional / structured / modern.

Target Market(s)

BtoB; Oil and gas companies; French speaking copying established in Angola, all industrials, factories and importers of goods.

Industry/Entity Type

Insurance Broker

Font styles to use
Sans Serif

Colors

Designer to choose colors to be used in the design.

Requirements
Must have
• We need something respecting the colors of our orange logtype; blue; white; black; easy to scroll, with simple information on the company; - who we are - our team (with the pictures) - what we do - what we do - contact us, contact us (google map) Luanda (Angola) Small company, just need something flashy / professional / structured / modern.
Nice to have
• A page format
Should not have
• WE DO NOT WANT A REFER TO OUR LOGO, but a Home Page for our Website with the basics categories ... >> PLEASE CAREFULLY USE THE RIGHT COLOR OF THE LOGOTYPE which are the ones enclosed Orange / Turquoise / Black as per the business card .

```html
<!DOCTYPE html>
<html lang="en">
<head>
<meta charset="utf-8">
<title>Tavlin-Brokers — Insurance Brokerage</title>
<link href="https://fonts.googleapis.com/css2?family=Audiowide&family=Poppins:wght@400;500;600;700&display=swap" rel="stylesheet">
<style>
:root{
  --orange:#f04e23;
  --orange-light:#ff6a3d;
  --blue:#1e8fd8;
  --blue-light:#3fb0ea;
  --green:#1b8a3a;
  --ink:#1a1a1a;
  --text:#555;
  --soft:#f1f2f1;
  --white:#fff;
}
*{margin:0;padding:0;box-sizing:border-box}
html,body{width:1200px;height:3494px;overflow:hidden}
body{position:relative;background:var(--white);font-family:'Poppins',sans-serif;color:var(--ink)}
.abs{position:absolute}
.heading{font-family:'Audiowide',sans-serif;font-weight:400;letter-spacing:1px;color:var(--ink)}

/* header */
.brand{left:145px;top:70px;font-size:24px;font-weight:700;color:var(--green);display:flex;align-items:center;gap:10px}
.brand-dot{width:44px;height:44px;border-radius:50%;background:var(--blue)}
.call{right:143px;top:28px;display:flex;align-items:center;gap:10px}
.call-icon{width:38px;height:38px}
.call small{color:var(--orange);font-size:16px}
.call strong{font-size:27px;font-weight:700;color:var(--ink)}
.nav{left:397px;top:91px;width:803px;height:40px}
.nav-links{left:430px;top:91px;display:flex;height:40px}
.nav-links a{color:var(--white);text-decoration:none;font-size:17px;line-height:40px;padding:0 16px}

/* hero */
.hero{left:0;top:131px;width:1200px;height:615px;background:linear-gradient(180deg,#7b8896 0%,#6a7a88 35%,#4c5d6b 70%,#3d4a55 100%)}
.hero-title{left:0;width:1200px;top:312px;text-align:center;font-size:60px;color:var(--white);letter-spacing:3px}
.hero-sub{left:0;width:1200px;top:396px;text-align:center;font-size:18px;color:var(--white)}
.btn{display:flex;align-items:center;gap:10px;background:linear-gradient(90deg,var(--orange),var(--orange-light));color:var(--white);font-weight:700;border-radius:30px;padding:5px 22px 5px 5px;font-size:17px;box-shadow:0 3px 8px rgba(0,0,0,.25)}
.btn i{width:38px;height:38px;border-radius:50%;background:var(--white);display:block}
.hero-btn{left:505px;top:458px}
.dots{left:548px;top:643px;display:flex;gap:7px}
.dots span{width:15px;height:15px;border-radius:50%;background:var(--white)}
.dots span.on{background:transparent;border:3px solid var(--white)}

/* who */
.who-h{left:145px;top:830px;font-size:42px}
.who-p{left:145px;top:893px;width:450px;font-size:12.4px;line-height:30.5px;color:var(--text);letter-spacing:-0.1px}
.who-btn{left:145px;top:1133px;font-size:15px}
.who-img{left:655px;top:808px;width:400px;height:400px;border-radius:50%;background:linear-gradient(135deg,#dfe6e3,#8fa39e 60%,#4b5f63)}

/* team */
.team-bg{left:-180px;top:1278px;width:1560px;height:650px;border-radius:50%;background:var(--soft)}
.team-h{left:0;width:1200px;top:1393px;text-align:center;font-size:42px}
.member{top:1488px;width:230px;text-align:center}
.member .photo{width:188px;height:188px;margin:0 auto;border-radius:50%;border:4px solid var(--orange);padding:8px;background:var(--white)}
.member .photo div{width:100%;height:100%;border-radius:50%;background:linear-gradient(160deg,#c9c2b7,#6e6a66)}
.member h3{margin-top:14px;font-size:20px;font-weight:600}
.member p{font-size:14px;color:var(--text);margin-top:2px}
.member .social{font-size:13px;color:var(--blue);font-weight:600;margin-top:6px}

/* services */
.do-h{left:0;width:1200px;top:2012px;text-align:center;font-size:42px}
.card{width:428px;height:152px;border-radius:76px;background:var(--white);box-shadow:0 4px 16px rgba(0,0,0,.12)}
.card .icon{position:absolute;left:14px;top:24px;width:104px;height:104px;border-radius:50%;box-shadow:0 2px 10px rgba(0,0,0,.12);background:var(--white)}
.card .icon svg{position:absolute;left:27px;top:27px}
.card .body{position:absolute;left:140px;top:24px;width:280px}
.card h4{font-size:19px;font-weight:500;line-height:24px;white-space:nowrap}
.card p{font-size:13px;color:var(--text);line-height:21px;margin-top:8px}
.card a{display:block;font-size:13px;color:var(--orange);font-weight:600;margin-top:8px;text-decoration:none}

/* contact */
.contact-svg{left:0;top:2540px}
.contact-h{left:0;width:1200px;top:2660px;text-align:center;font-size:42px;color:var(--white)}
.field{background:var(--white);font-size:14px;color:#555;padding:13px 21px;height:46px}
.submit{left:500px;top:3026px;font-size:16px}

/* info */
.info{top:3227px;width:240px;text-align:center}
.info .ring{width:72px;height:72px;margin:0 auto;border-radius:50%;border:2px solid var(--blue);display:flex;align-items:center;justify-content:center}
.info .ring.fill{background:var(--orange);border-color:var(--orange)}
.info h5{font-size:16px;font-weight:600;margin-top:20px}
.info p{font-size:13px;color:var(--text);line-height:22px;margin-top:4px}

/* footer */
.rule{left:145px;top:3425px;width:910px;height:1px;background:#ddd}
.copy{left:145px;top:3450px;font-size:13px;color:var(--text)}
.foot-links{left:900px;top:3450px;width:155px;text-align:right;font-size:13px;color:var(--blue);font-weight:600}
</style>
</head>
<body>

<!-- header -->
<div class="abs brand"><span class="brand-dot"></span>TAVLIN-BROKERS</div>
<div class="abs call">
  <svg class="call-icon" viewBox="0 0 38 38"><circle cx="19" cy="19" r="17" fill="none" stroke="#1b8a3a" stroke-width="2.5"/><path d="M13 11c1-1 2-1 3 0l2 3c.5 1 0 2-1 2.5 1 2.5 3 4.5 5.5 5.5.5-1 1.5-1.5 2.5-1l3 2c1 1 1 2 0 3l-1.5 1.5c-6 0-14-8-14-14z" fill="#1b8a3a"/></svg>
  <small>CALL US :</small><strong>1 555 014 2290</strong>
</div>
<svg class="abs nav" viewBox="0 0 803 40" width="803" height="40">
  <defs><linearGradient id="navg" x1="0" x2="1"><stop offset="0" stop-color="#1e8fd8"/><stop offset=".1" stop-color="#3fb0ea"/><stop offset=".1" stop-color="#f04e23"/><stop offset="1" stop-color="#ff5a2c"/></linearGradient></defs>
  <path d="M28 0H803V40H0Z" fill="url(#navg)"/>
</svg>
<nav class="abs nav-links"><a>Home</a><a>Who we are</a><a>Our team</a><a>What we do</a><a>Contact us</a></nav>

<!-- hero -->
<div class="abs hero" role="img" aria-label="Aerial photograph of a coastal city skyline with high-rise towers"></div>
<h1 class="abs heading hero-title">TAVLIN BROKERS</h1>
<p class="abs hero-sub">Lorem ipsum dolor sit amet consectetur adipiscing elit</p>
<div class="abs btn hero-btn"><i></i>GET STARTED</div>
<div class="abs dots"><span></span><span></span><span class="on"></span><span></span><span></span></div>
<svg class="abs" style="left:0;top:560px" width="1200" height="200" viewBox="0 0 1200 200">
  <path d="M0 50 C300 140 600 150 1200 10 L1200 40 C600 190 300 180 0 85 Z" fill="#1e8fd8"/>
  <path d="M0 85 C300 180 600 190 1200 40 L1200 200 L0 200 Z" fill="#fff"/>
</svg>

<!-- who we are -->
<h2 class="abs heading who-h">WHO WE ARE</h2>
<p class="abs who-p">Lorem ipsum dolor sit amet, consectetur adipiscing elid do eiusmod tempor incididunt ut labore et dolore magna aliqua enim ad minim veniam, quis nostrud exercitation ullamco laboris nisi ut aliquip ex ea commodo consequat. Duis aute irure dolor in reprehenderivoluptate velit esse cillum dolore eu fugiat nulla pariatucepteur sint occaecat cupidatat non proident, sunt in culpa qui officia deserunt mollit anii d est laborumoccaecat cupidatat non proident.</p>
<div class="abs btn who-btn"><i></i>READ MORE</div>
<div class="abs who-img" role="img" aria-label="Circular photograph of a team working at an office desk"></div>

<!-- team -->
<div class="abs team-bg"></div>
<h2 class="abs heading team-h">OUR TEAM</h2>
<div class="abs member" style="left:125px"><div class="photo"><div role="img" aria-label="Portrait photo of John Doe"></div></div><h3>JOHN DOE</h3><p>Lorem ipsum dolor sit amet</p><div class="social">Fb · Tw · In</div></div>
<div class="abs member" style="left:371px"><div class="photo"><div role="img" aria-label="Portrait photo of Smitha"></div></div><h3>SMITHA</h3><p>Lorem ipsum dolor sit amet</p><div class="social">Fb · Tw · In</div></div>
<div class="abs member" style="left:610px"><div class="photo"><div role="img" aria-label="Portrait photo of Josnag"></div></div><h3>JOSNAG</h3><p>Lorem ipsum dolor sit amet</p><div class="social">Fb · Tw · In</div></div>
<div class="abs member" style="left:848px"><div class="photo"><div role="img" aria-label="Portrait photo of Labris"></div></div><h3>LABRIS</h3><p>Lorem ipsum dolor sit amet</p><div class="social">Fb · Tw · In</div></div>

<!-- what we do -->
<h2 class="abs heading do-h">WHAT WE DO</h2>
<div class="abs card" style="left:145px;top:2115px">
  <div class="icon"><svg width="50" height="50" viewBox="0 0 50 50" fill="none" stroke="#1e8fd8" stroke-width="2"><path d="M20 6l14 5v12c0 10-7 17-14 20C13 40 6 33 6 23V11z"/><path d="M14 24l5 5 9-10"/></svg></div>
  <div class="body"><h4>LIABILITIES INSURANCES</h4><p>Sed ut perspiciatis unde omnis iste nat<br>voluptatem accusantium</p><a>Read More »</a></div>
</div>
<div class="abs card" style="left:627px;top:2115px">
  <div class="icon"><svg width="50" height="50" viewBox="0 0 50 50" fill="none" stroke="#1e8fd8" stroke-width="2"><path d="M12 22l4-10h18l4 10"/><rect x="6" y="22" width="38" height="14" rx="3"/><circle cx="14" cy="29" r="2.5"/><circle cx="36" cy="29" r="2.5"/><path d="M10 36v6h6v-6M34 36v6h6v-6"/></svg></div>
  <div class="body"><h4>AUTOMOBILE INSURANCES</h4><p>Sed ut perspiciatis unde omnis iste nat<br>voluptatem accusantium</p><a>Read More »</a></div>
</div>
<div class="abs card" style="left:145px;top:2308px">
  <div class="icon"><svg width="50" height="50" viewBox="0 0 50 50" fill="none" stroke="#1e8fd8" stroke-width="2"><circle cx="25" cy="25" r="13"/><circle cx="25" cy="25" r="6"/><path d="M25 4v6M25 40v6M4 25h6M40 25h6M10 10l4 4M36 36l4 4M40 10l-4 4M14 36l-4 4"/></svg></div>
  <div class="body"><h4>CONSTRUCTION &amp;<br>ENGINEERING CASUALTY.</h4><p>Sed ut perspiciatis unde omnis iste nat</p><a>Read More »</a></div>
</div>
<div class="abs card" style="left:627px;top:2308px">
  <div class="icon"><svg width="50" height="50" viewBox="0 0 50 50" fill="none" stroke="#1e8fd8" stroke-width="2"><rect x="10" y="4" width="26" height="40" rx="2"/><path d="M16 14h14M16 20h14M16 26h8"/><rect x="24" y="28" width="20" height="14" rx="2"/><path d="M24 33h20"/></svg></div>
  <div class="body"><h4>MARIME &amp; TRANSIT<br>CREDIT INSURANCE YOUNG</h4><p>Sed ut perspiciatis unde omnis iste nat</p><a>Read More »</a></div>
</div>

<!-- contact -->
<svg class="abs contact-svg" width="1200" height="680" viewBox="0 0 1200 680">
  <defs><linearGradient id="mapg" x1="0" y1="0" x2="1" y2="1"><stop offset="0" stop-color="#3fa6e4"/><stop offset=".6" stop-color="#4aa8d8"/><stop offset="1" stop-color="#6fb3c9"/></linearGradient></defs>
  <path role="img" aria-label="Street map of the Luanda area tinted blue" d="M0 180 C250 40 700 0 1000 60 C1120 90 1180 130 1200 160 L1200 420 C1000 640 400 700 0 540 Z" fill="url(#mapg)"/>
  <path d="M660 6 C900 10 1100 60 1200 140" fill="none" stroke="#1b8a3a" stroke-width="6"/>
  <path d="M0 510 C150 600 350 650 560 655" fill="none" stroke="#1b8a3a" stroke-width="6"/>
</svg>
<h2 class="abs heading contact-h">CONTACT US</h2>
<div class="abs field" style="left:229px;top:2748px;width:362px">Enter Name</div>
<div class="abs field" style="left:608px;top:2748px;width:363px">Enter Email</div>
<div class="abs field" style="left:229px;top:2815px;width:362px">Address</div>
<div class="abs field" style="left:608px;top:2815px;width:363px">Phone</div>
<div class="abs field" style="left:229px;top:2883px;width:742px;height:107px">Message</div>
<div class="abs btn submit"><i></i>SUBMIT MESSAGE</div>

<!-- contact info -->
<div class="abs info" style="left:83px"><div class="ring"><svg width="30" height="30" viewBox="0 0 30 30"><path d="M7 5c1-1 2-1 3 0l2.5 3.5c.5 1 0 2-1 2.5 1 3 3.5 5.5 6.5 6.5.5-1 1.5-1.5 2.5-1l3.5 2.5c1 1 1 2 0 3l-2 2c-7 0-15-8-15-15z" fill="#f04e23"/></svg></div><h5>PHONE</h5><p>(+244) 555 014 2290</p></div>
<div class="abs info" style="left:317px"><div class="ring"><svg width="30" height="30" viewBox="0 0 30 30"><path d="M15 3a8 8 0 0 1 8 8c0 6-8 16-8 16S7 17 7 11a8 8 0 0 1 8-8z" fill="#f04e23"/><circle cx="15" cy="11" r="3" fill="#fff"/></svg></div><h5>HEAD OFFICE</h5><p>48 Marlow Harbour Lane, Ingombota,<br>Luanda, Angola. CP 1120</p></div>
<div class="abs info" style="left:602px"><div class="ring fill"><svg width="30" height="30" viewBox="0 0 30 30"><path d="M15 3a8 8 0 0 1 8 8c0 6-8 16-8 16S7 17 7 11a8 8 0 0 1 8-8z" fill="#fff"/><circle cx="15" cy="11" r="3" fill="#f04e23"/></svg></div><h5>MAIN OFFICE</h5><p>210 Kestrel Avenue, Talatona,<br>Luanda, Angola. CP 3305</p></div>
<div class="abs info" style="left:863px"><div class="ring"><svg width="30" height="30" viewBox="0 0 30 30"><rect x="4" y="7" width="22" height="16" rx="2" fill="#f04e23"/><path d="M5 9l10 7 10-7" fill="none" stroke="#fff" stroke-width="1.8"/></svg></div><h5>EMAIL</h5><p>info@tavlinbrokers.com</p></div>

<!-- footer -->
<div class="abs rule"></div>
<p class="abs copy">Copyrights © 2019, Tavlin Brokers.All rights reserved &nbsp;|&nbsp; Privacy Policy &nbsp;|&nbsp; Terms of use</p>
<div class="abs foot-links">Fb · Tw · G</div>

</body>
</html>
```